Business Card Design Needed

Business car design required, logo will be supplied.

Brackenfield Heat Surveyors are looking to become the leading provider of energy performance certificates to estate agents, landlords and home owners in the Yorkshire region of the UK.

The business card must be double sided and professional looking. Estate agents receive hundreds of cards from contractors and our card must stand out.

I require a two sided business card that is clean, modern and created by a designer that can think outside of the box.

Brand colours can be supplied .

Please ask if you have any questions.

Target Market(s)

Estate agents, landlords and property owners

Industry/Entity Type

Property - estate agency - energy consultants

Contact Information for Business Card

Tomas Birchwell - Energy Assessor - 07351642170 - www.BrackenfieldHSV.co.uk - info@brackenfieldhsv.co.uk

Font styles to use
Serif
Sans Serif

Colors
00AB8E
00BBA5
67D7C9
C6EFE9
E9F9F6

Requirements
Must have
• Use the provided logo, clean, professional and stand out from the crowd
Nice to have
• Clever use of text, spacing and brand colours
Should not have
• Clip art

```html
<!DOCTYPE html>
<html lang="en">
<head>
<meta charset="utf-8">
<title>Brackenfield Heat Surveyors – Business Card</title>
<link href="https://fonts.googleapis.com/css2?family=Montserrat:wght@600;700&family=Open+Sans:wght@400;600&display=swap" rel="stylesheet">
<style>
  :root {
    --brand-blue: #0b6bab;
    --brand-blue-deep: #075a93;
    --brand-lime: #b4cf1e;
    --paper: #f7f7f5;
    --ink-grey: #5a5a5a;
    --backdrop: #e4e6e8;
    --white: #ffffff;
  }
  * { margin: 0; padding: 0; box-sizing: border-box; }
  html, body {
    width: 1200px; height: 874px; overflow: hidden;
    background: var(--backdrop);
  }
  .canvas {
    position: relative; width: 1200px; height: 874px;
    display: flex; flex-direction: column; align-items: center; justify-content: center;
    gap: 44px;
  }
  .card {
    position: relative; width: 600px; height: 343px;
    border-radius: 26px; overflow: hidden;
  }

  /* Front side */
  .card--front {
    background: var(--brand-blue);
    display: flex; align-items: center; justify-content: center; gap: 20px;
  }
  .brand-dot {
    width: 54px; height: 54px; border-radius: 50%;
    background: var(--brand-lime);
    flex: none;
  }
  .brand-divider {
    width: 1px; height: 62px; background: rgba(255,255,255,0.7);
  }
  .brand-name {
    font-family: "Montserrat", sans-serif; font-weight: 600;
    font-size: 27px; letter-spacing: 0.5px;
    color: var(--white);
  }

  /* Back side */
  .card--back { background: var(--paper); }
  .swoosh { position: absolute; left: 0; bottom: 0; width: 600px; height: 343px; }
  .contact {
    position: absolute; left: 38px; top: 120px;
  }
  .contact__name {
    font-family: "Montserrat", sans-serif; font-weight: 700;
    font-size: 24px; color: var(--brand-blue); letter-spacing: 0.3px;
    line-height: 1;
  }
  .contact__role {
    font-family: "Open Sans", sans-serif; font-weight: 400;
    font-size: 15px; color: var(--brand-lime); margin-top: 2px;
  }
  .rule {
    position: absolute; left: 38px; top: 168px; width: 490px; height: 2px;
    background: var(--brand-blue);
  }
  .contact-list {
    position: absolute; left: 38px; top: 180px; list-style: none;
    font-family: "Open Sans", sans-serif; font-size: 15px; color: var(--ink-grey);
  }
  .contact-list li { display: flex; align-items: center; gap: 9px; line-height: 24px; }
  .contact-list svg { width: 13px; height: 13px; fill: var(--brand-lime); flex: none; }
  .website {
    position: absolute; right: 72px; top: 232px;
    font-family: "Open Sans", sans-serif; font-size: 15px; color: var(--brand-blue);
  }
  .website strong { font-weight: 600; }
  .mark {
    position: absolute; right: 56px; top: 34px;
    display: flex; flex-direction: column; align-items: center; gap: 8px;
  }
  .mark__circle {
    width: 104px; height: 104px; border-radius: 50%;
    border: 10px solid var(--brand-blue);
  }
  .mark__name {
    font-family: "Montserrat", sans-serif; font-weight: 600;
    font-size: 10px; color: var(--brand-blue); letter-spacing: 0.3px;
  }
</style>
</head>
<body>
<main class="canvas">
  <section class="card card--front" aria-label="Card front">
    <span class="brand-dot"></span>
    <span class="brand-divider"></span>
    <span class="brand-name">Brackenfield Heat Surveyors</span>
  </section>

  <section class="card card--back" aria-label="Card back">
    <svg class="swoosh" viewBox="0 0 600 343" aria-hidden="true">
      <path d="M0 250 Q 260 330 600 330 L600 343 L0 343 Z" fill="var(--brand-blue)"/>
      <path d="M290 312 Q 460 322 600 306" fill="none" stroke="var(--brand-lime)" stroke-width="6"/>
    </svg>

    <div class="mark">
      <span class="mark__circle"></span>
      <span class="mark__name">Brackenfield Heat Surveyors</span>
    </div>

    <div class="contact">
      <h1 class="contact__name">TOMAS BIRCHWELL</h1>
      <p class="contact__role">Energy Assessor</p>
    </div>
    <div class="rule"></div>
    <ul class="contact-list">
      <li>
        <svg viewBox="0 0 24 24"><path d="M6.6 10.8a15.1 15.1 0 0 0 6.6 6.6l2.2-2.2c.3-.3.7-.4 1-.2 1.1.4 2.3.6 3.6.6.6 0 1 .4 1 1V20c0 .6-.4 1-1 1A17 17 0 0 1 3 4c0-.6.4-1 1-1h3.5c.6 0 1 .4 1 1 0 1.3.2 2.5.6 3.6.1.3 0 .7-.2 1z"/></svg>
        07351642170
      </li>
      <li>
        <svg viewBox="0 0 24 24"><path d="M2 5h20v14H2z M2 5l10 8 10-8" /></svg>
        info@brackenfieldhsv.co.uk
      </li>
    </ul>
    <p class="website">www.<strong>BrackenfieldHSV</strong>.co.uk</p>
  </section>
</main>
</body>
</html>
```